Need Business Cards for my Business

email address: rkpmarlowhollowworks@vendrimail.com
web address: rkpmarlowhollowworks.net
Slogan: We offer various QVN licenses
Rowland K. Pemberly
Please stick with colors of Company Logo
would like the card to be more of the color example of the logo.
If you need PDF copy of logo email me at the above account.
Creative control rests with you.

Industry/Entity Type

Business

Contact Information for Business Card

I am a minimalist, but would like something to pop and stand out amongst other cards, make it memorable.

Font styles to use
Serif
Decorative
Script

```html
<!DOCTYPE html>
<html lang="en">
<head>
<meta charset="utf-8">
<title>RKP Marlow Hollow – Business Cards</title>
<link href="https://fonts.googleapis.com/css2?family=Arimo:wght@400;700&family=Michroma&display=swap" rel="stylesheet">
<style>
  :root {
    --backdrop: #1e1f21;
    --card: #ffffff;
    --navy: #1d4478;
    --red: #e42a2f;
    --grey: #6f7277;
    --ink: #3a3c40;
  }
  * { box-sizing: border-box; margin: 0; padding: 0; }
  html, body {
    width: 1200px;
    height: 950px;
    overflow: hidden;
  }
  body {
    background: var(--backdrop);
    font-family: "Arimo", Arial, sans-serif;
    display: flex;
    flex-direction: column;
    align-items: center;
    justify-content: center;
    gap: 30px;
  }
  .card {
    position: relative;
    width: 760px;
    height: 434px;
    background: var(--card);
    overflow: hidden;
  }

  /* Brand name lockup */
  .brand {
    display: flex;
    align-items: center;
    gap: 14px;
  }
  .brand-dot {
    width: 34px;
    height: 34px;
    border-radius: 50%;
    background: var(--red);
    flex: none;
  }
  .brand-name {
    font-family: "Arimo", Arial, sans-serif;
    font-weight: 700;
    color: var(--navy);
    font-size: 40px;
    letter-spacing: 1px;
    line-height: 1;
  }

  /* Front side */
  .card-front {
    display: flex;
    flex-direction: column;
    align-items: center;
    justify-content: center;
    text-align: center;
  }
  .card-front .brand { margin-bottom: 16px; }
  .slogan {
    color: var(--red);
    font-size: 22px;
    font-weight: 400;
    margin-bottom: 48px;
  }
  .license-list {
    color: var(--grey);
    font-size: 18px;
    line-height: 1.35;
    list-style: none;
  }
  .license-list .sep { margin: 0 6px; }

  /* Back side */
  .card-back {
    border-top: 12px solid var(--red);
    border-bottom: 14px solid var(--navy);
    padding: 78px 0 0 70px;
  }
  .card-back .brand-name { font-size: 44px; }
  .person { margin-top: 50px; }
  .person-name {
    font-family: "Michroma", Arial, sans-serif;
    color: var(--navy);
    font-size: 24px;
    letter-spacing: 2px;
  }
  .person-role {
    font-family: "Michroma", Arial, sans-serif;
    color: var(--red);
    font-size: 15px;
    letter-spacing: 1.5px;
    margin-top: 6px;
  }
  .contact-list {
    list-style: none;
    margin-top: 22px;
  }
  .contact-list li {
    display: flex;
    align-items: center;
    gap: 12px;
    color: var(--grey);
    font-size: 19px;
    line-height: 1.55;
  }
  .contact-icon {
    width: 18px;
    height: 18px;
    fill: var(--ink);
    flex: none;
  }
</style>
</head>
<body>

  <section class="card card-front" aria-label="Card front">
    <div class="brand">
      <span class="brand-dot"></span>
      <span class="brand-name">RKP Marlow Hollow</span>
    </div>
    <p class="slogan">We offer various QVN licenses</p>
    <ul class="license-list">
      <li>General Radiotelephone Operator License</li>
      <li>Marine Radio Operator License Permit<span class="sep">•</span>GMDSS Radio Operators License</li>
      <li>GMDSS Radio Maintainers License<span class="sep">•</span>Ship Radar Endorsement</li>
    </ul>
  </section>

  <section class="card card-back" aria-label="Card back">
    <div class="brand">
      <span class="brand-dot"></span>
      <span class="brand-name">RKP Marlow Hollow</span>
    </div>
    <div class="person">
      <p class="person-name">Rowland K. Pemberly</p>
      <p class="person-role">CEO/Founder</p>
    </div>
    <ul class="contact-list">
      <li>
        <svg class="contact-icon" viewBox="0 0 24 24" aria-hidden="true"><path d="M3 9c0-3 4-5 9-5s9 2 9 5l-1 2-4-1v-2c-2-.6-6-.6-8 0v2l-4 1zM6 13h12l2 7H4z"/></svg>
        555-204-7781
      </li>
      <li>
        <svg class="contact-icon" viewBox="0 0 24 24" aria-hidden="true"><path d="M7 1h10a2 2 0 0 1 2 2v18a2 2 0 0 1-2 2H7a2 2 0 0 1-2-2V3a2 2 0 0 1 2-2zm0 3v14h10V4zm5 15.5a1.2 1.2 0 1 0 0 2.4 1.2 1.2 0 0 0 0-2.4z"/></svg>
        555 318 6620
      </li>
      <li>
        <svg class="contact-icon" viewBox="0 0 24 24" aria-hidden="true"><path d="M2 5h20v14H2zm2 2v.5l8 5.5 8-5.5V7z"/></svg>
        rkpmarlowhollowworks@vendrimail.com
      </li>
      <li>
        <svg class="contact-icon" viewBox="0 0 24 24" aria-hidden="true"><path d="M12 2a10 10 0 1 0 0 20 10 10 0 0 0 0-20zm-1 17.9A8 8 0 0 1 4.1 11H7c.2 3.3 1.6 6.4 4 8.9zm2 0c2.4-2.5 3.8-5.6 4-8.9h2.9A8 8 0 0 1 13 19.9zM9 11h6c-.2 2.7-1.3 5.2-3 7.2-1.7-2-2.8-4.5-3-7.2zm0-2c.2-2.7 1.3-5.2 3-7.2 1.7 2 2.8 4.5 3 7.2zm-4.9 0A8 8 0 0 1 11 4.1C8.6 6.6 7.2 9.7 7 13"/></svg>
        rkpmarlowhollowworks.net
      </li>
    </ul>
  </section>

</body>
</html>
```